36" inch (height) x 96" inch (width) Banner for Baseball Field

Hello. This project is an advertisement that will be printed onto a 3 foot by 8 foot full color banner and placed at little league fields in Southern California. A theme of the banner can be baseball. The company is my law office practicing Estate Planning and Tax Law. I am uploading the current business card, which has the logo, website, and telephone number. You can also pull images from www.rkpembrove.com I would like the banner to be a fun design that incorporates baseball somehow, but draws attention to my law and tax office, and my website. Please be creative, and have fun with it. The colors of my practice are included in the logo. At the bottom, it should say "Attorney Advertisement," but this can be in very small font in the bottom right or left corner.

Target Market(s)

Youth Baseball Fans

Industry/Entity Type

Law; Accounting

Colors

Designer to choose colors to be used in the design.

Requirements
Must have
• My telephone number. My website.
Nice to have
• Would like to see "Estate Planning" and "Tax Law and Preparation" Would also like to see "Attorney" and "CPA" or "Certified Public Accountant" prominently diplayed

```html
<!DOCTYPE html>
<html lang="en">
<head>
<meta charset="utf-8">
<title>RK Pembrove – Attorney &amp; CPA Banner</title>
<link href="https://fonts.googleapis.com/css2?family=Old+Standard+TT:wght@400;700&family=Oswald:wght@300;400;500&family=Quicksand:wght@300;400&family=Montserrat:wght@400;700&display=swap" rel="stylesheet">
<style>
  :root {
    --brand-blue: #2a98d4;
    --ink: #111111;
    --panel-black: #000000;
    --paper: #ffffff;
    --gold: #ecb97c;
  }
  * { margin: 0; padding: 0; box-sizing: border-box; }
  html, body { width: 1200px; height: 450px; overflow: hidden; background: var(--paper); }
  .banner { position: relative; width: 1200px; height: 450px; overflow: hidden; background: var(--paper); font-family: "Montserrat", sans-serif; }

  .rules { position: absolute; inset: 0; width: 1200px; height: 450px; }

  /* left identity panel */
  .identity { position: absolute; left: 0; top: 0; width: 458px; height: 450px; text-align: center; }
  .brand-mark { position: absolute; left: 152px; top: 50px; width: 148px; height: 148px; border-radius: 50%; border: 7px solid var(--brand-blue); display: flex; align-items: center; justify-content: center; font-family: "Old Standard TT", serif; font-weight: 700; font-size: 62px; color: var(--brand-blue); }
  .firm-intro { position: absolute; left: 0; width: 450px; top: 206px; font-family: "Old Standard TT", serif; font-size: 27px; color: var(--ink); letter-spacing: 0.5px; white-space: nowrap; }
  .firm-of { position: absolute; left: 0; width: 450px; top: 234px; font-family: "Old Standard TT", serif; font-size: 24px; color: var(--ink); }
  .firm-name { position: absolute; left: 0; width: 450px; top: 258px; font-family: "Old Standard TT", serif; font-size: 43px; color: var(--brand-blue); letter-spacing: 0.5px; white-space: nowrap; }
  .principal { position: absolute; left: 0; width: 450px; top: 306px; font-family: "Old Standard TT", serif; font-size: 19px; color: var(--ink); letter-spacing: 0.5px; white-space: nowrap; }
  .credentials { position: absolute; left: 0; width: 458px; top: 352px; font-family: "Old Standard TT", serif; font-size: 47px; color: var(--brand-blue); white-space: nowrap; }
  .disclaimer { position: absolute; right: 6px; top: 431px; font-size: 10.5px; color: #333; letter-spacing: 0.3px; white-space: nowrap; }

  /* right black panel */
  .panel { position: absolute; left: 458px; top: 35px; width: 742px; height: 415px; background: var(--panel-black); }
  .portrait { position: absolute; left: 468px; top: 12px; width: 390px; height: 438px; border-radius: 180px 180px 0 0; background: radial-gradient(ellipse at 50% 25%, #e6ebee 0%, #c9a48a 30%, #2a2a2a 62%, #111 100%); }

  .tagline { position: absolute; left: 705px; top: 320px; font-family: "Quicksand", sans-serif; font-weight: 300; font-size: 22px; line-height: 21px; color: var(--gold); white-space: nowrap; }
  .tagline-emphasis { position: absolute; left: 697px; top: 376px; font-family: "Oswald", sans-serif; font-weight: 300; transform: scaleX(0.55); transform-origin: left; font-size: 60px; line-height: 60px; letter-spacing: 22px; color: var(--gold); white-space: nowrap; }

  .services { position: absolute; right: 47px; top: 104px; text-align: right; color: var(--paper); font-family: "Quicksand", sans-serif; font-size: 33px; line-height: 34px; }
  .services .line { position: relative; height: 36px; white-space: nowrap; }
  .services .boxed { display: inline-block; background: var(--paper); color: var(--ink); font-family: "Montserrat", sans-serif; font-weight: 700; font-size: 27px; padding: 0 6px; line-height: 36px; }
  .services .line-two .boxed { padding: 2px 8px; }
  .ball { position: absolute; right: -22px; top: 14px; width: 9px; height: 9px; border-radius: 50%; background: var(--paper); }

  .location { position: absolute; left: 880px; width: 300px; top: 186px; text-align: center; font-family: "Oswald", sans-serif; font-weight: 500; color: var(--gold); white-space: nowrap; }
  .location .pin { display: block; margin: 0 auto 6px; }
  .location .addr { font-size: 19px; line-height: 22px; letter-spacing: 0.5px; }
  .location .state { font-size: 28px; line-height: 34px; color: var(--paper); letter-spacing: 1px; }

  .contact { position: absolute; left: 880px; width: 300px; top: 340px; font-family: "Oswald", sans-serif; font-size: 19px; color: var(--paper); white-space: nowrap; }
  .contact .row { display: flex; align-items: center; justify-content: center; gap: 5px; height: 26px; white-space: nowrap; }
  .contact .mobile { color: var(--gold); }
  .contact .divider { height: 1px; background: #888; width: 222px; margin: 10px auto 6px; }
  .contact .web-row { font-family: "Montserrat", sans-serif; font-size: 11.5px; }
  .contact .site { color: var(--gold); }
  .contact .spacer { width: 8px; }
</style>
</head>
<body>
<div class="banner">
  <svg class="rules" viewBox="0 0 1200 450" aria-hidden="true">
    <path d="M0 20 H300 Q330 20 345 30 Q352 35 365 35 H458" fill="none" stroke="#333" stroke-width="1"/>
    <path d="M6 352 H30 Q40 352 50 346 Q60 338 75 338 H400 Q410 338 418 333 Q425 329 436 329 H456" fill="none" stroke="#333" stroke-width="1"/>
    <path d="M0 443 H320" fill="none" stroke="#333" stroke-width="1"/>
    <path d="M402 282 H460" fill="none" stroke="#999" stroke-width="1"/>
    <path d="M140 257 L210 255 M240 255 L316 257" stroke="#111" stroke-width="2.5"/>
    <g fill="none" stroke="#111" stroke-width="3"><circle cx="214" cy="338" r="5.5"/><circle cx="231" cy="338" r="5.5"/><circle cx="248" cy="338" r="5.5"/></g>
  </svg>

  <section class="identity">
    <div class="brand-mark">RK</div>
    <div class="firm-intro">THE LAW OFFICES</div>
    <div class="firm-of">OF</div>
    <div class="firm-name">RK PEMBROVE</div>
    <div class="principal">Rowan K Pembrove</div>
    <div class="credentials">ATTORNEY &amp; CPA</div>
    <div class="disclaimer">Attorney Advertisement</div>
  </section>

  <div class="panel"></div>
  <div class="portrait" role="img" aria-label="Photo of the attorney in a dark suit wearing a white batting helmet with face guard"></div>
  <svg class="rules" viewBox="0 0 1200 450" aria-hidden="true">
    <path d="M460 282 H470 Q480 282 492 272 Q510 246 540 245 H572" fill="none" stroke="#aaa" stroke-width="1"/>
    <circle cx="574" cy="244" r="2.5" fill="none" stroke="#fff" stroke-width="1"/>
  </svg>

  <div class="tagline">It is not wisdom<br>but Authority<br>that makes</div>
  <div class="tagline-emphasis">A LAW</div>

  <div class="services">
    <div class="line">Estate <span class="boxed">Planning</span><span class="ball"></span></div>
    <div class="line line-two"><span class="boxed">Tax Law</span> and Preparation<span class="ball"></span></div>
  </div>

  <div class="location">
    <svg class="pin" width="16" height="24" viewBox="0 0 16 24"><path d="M8 0 C3.5 0 0 3.5 0 8 C0 14 8 24 8 24 C8 24 16 14 16 8 C16 3.5 12.5 0 8 0 Z" fill="var(--gold)"/><circle cx="8" cy="8" r="3.2" fill="#000"/></svg>
    <div class="addr">728 HARLOW AVENUE</div>
    <div class="addr">PENTHOUSE SUITE 220</div>
    <div class="addr">CEDAR RIDGE,</div>
    <div class="state">CALIFORNIA&nbsp; 91377</div>
  </div>

  <div class="contact">
    <div class="row">
      <svg width="16" height="18" viewBox="0 0 24 24"><path d="M6.6 10.8a15 15 0 0 0 6.6 6.6l2.2-2.2a1 1 0 0 1 1-.25 11.4 11.4 0 0 0 3.6.57 1 1 0 0 1 1 1V20a1 1 0 0 1-1 1A17 17 0 0 1 3 4a1 1 0 0 1 1-1h3.5a1 1 0 0 1 1 1c0 1.25.2 2.45.57 3.57a1 1 0 0 1-.25 1z" fill="#fff"/></svg>
      <span>(555) 240-1836</span>
      <span class="spacer"></span>
      <svg width="12" height="19" viewBox="0 0 14 20"><rect x="1" y="1" width="12" height="18" rx="2" fill="none" stroke="var(--gold)" stroke-width="1.8"/><line x1="5" y1="16" x2="9" y2="16" stroke="var(--gold)" stroke-width="1.5"/></svg>
      <span class="mobile">(555) 318-4702</span>
    </div>
    <div class="row">
      <svg width="17" height="15" viewBox="0 0 18 16"><rect x="4" y="1" width="9" height="5" fill="none" stroke="#fff" stroke-width="1.5"/><rect x="1" y="6" width="16" height="9" rx="1" fill="#fff"/><rect x="5" y="9" width="8" height="2" fill="#000"/></svg>
      <span>(555) 472-9051</span>
    </div>
    <div class="divider"></div>
    <div class="row web-row">
      <svg width="12" height="9" viewBox="0 0 12 9"><rect x="0.5" y="0.5" width="11" height="8" fill="none" stroke="#fff"/><path d="M0.5 0.5 L6 5 L11.5 0.5" fill="none" stroke="#fff"/></svg>
      <span>rowan@rkpembrove.com</span>
      <span class="spacer"></span>
      <svg width="11" height="11" viewBox="0 0 12 12"><circle cx="6" cy="6" r="5" fill="none" stroke="var(--gold)"/><ellipse cx="6" cy="6" rx="2.2" ry="5" fill="none" stroke="var(--gold)"/><line x1="1" y1="6" x2="11" y2="6" stroke="var(--gold)"/></svg>
      <span class="site">www.rkpembrove.com</span>
    </div>
  </div>
</div>
</body>
</html>
```